Logo & Stationery Design

We are a new company based in Sydney, Australia called Brivana Fresh Pantry. We import and distribute top quality olive oil to restaurants and deli's, etc.
We need a logo design, business cards and letterheads for our company.
For the logo we would like to see designs that include an olive branch (olives and leaves) and that include the colours green and purple. Please see examples attached.
We would like a health, wellness and nature feel in the design.
For the business cards and letterheads we would like to add an illustration with a tag line. We would like to see something along the lines of oil dripping from an olive into a champagne glass with the tag line "top drop"

```html
<!DOCTYPE html>
<html lang="en">
<head>
<meta charset="utf-8">
<title>Brivana Fresh Pantry – Logo &amp; Stationery</title>
<link href="https://fonts.googleapis.com/css2?family=Questrial&display=swap" rel="stylesheet">
<style>
  :root {
    --olive: #6b8c21;
    --olive-line: #86a53a;
    --leaf-pale: #e4edc8;
    --leaf-on-dark: rgba(255,255,255,0.16);
    --paper: #ffffff;
    --ink: #4a4a4a;
    --ink-soft: #6a6a6a;
    --stage: #ffffff;
  }
  * { margin: 0; padding: 0; box-sizing: border-box; }
  html, body { width: 1200px; height: 1000px; overflow: hidden; background: var(--stage); }
  body { position: relative; font-family: "Questrial", sans-serif; color: var(--ink); }

  .wordmark {
    position: absolute;
    font-family: "Questrial", sans-serif;
    font-weight: 400;
    line-height: 1.02;
    text-align: center;
    display: flex; flex-direction: column; align-items: center; justify-content: center;
  }
  .wordmark-dot {
    display: block;
    width: 0.42em; height: 0.42em;
    border-radius: 50%;
    background: currentColor;
    margin-bottom: 0.18em;
  }
  .wordmark--on-white { left: 50px; top: 165px; width: 190px; height: 205px; font-size: 44px; color: var(--olive); }
  .wordmark-tile { position: absolute; background: var(--olive); z-index: 2; }
  .wordmark-tile--large { left: 265px; top: 156px; width: 232px; height: 230px; }
  .wordmark-tile .wordmark { inset: 0; color: var(--paper); }
  .wordmark-tile--large .wordmark { font-size: 45px; }

  .card, .letterhead {
    position: absolute;
    overflow: hidden;
    box-shadow: 0 1px 6px rgba(0,0,0,0.35);
  }
  .card { width: 204px; height: 367px; top: 488px; }
  .card--light { left: 48px; background: var(--paper); color: var(--olive); }
  .card--dark { left: 306px; background: var(--olive); color: var(--paper); }
  .card .wordmark-tile { left: 18px; top: 19px; width: 99px; height: 98px; }
  .card--dark .wordmark-tile { left: 16px; top: 17px; border: 1px solid var(--olive-line); box-shadow: 0 1px 3px rgba(0,0,0,0.25); }
  .card .wordmark-tile .wordmark { font-size: 18px; }

  .branch-decor { position: absolute; z-index: 0; }
  .card--light .branch-decor {
    left: 0; top: 110px; width: 204px; height: 257px;
    background: radial-gradient(ellipse 70% 60% at 35% 45%, var(--leaf-pale) 0%, rgba(228,237,200,0.55) 55%, rgba(228,237,200,0) 100%);
  }
  .card--dark .branch-decor {
    left: 0; top: 100px; width: 204px; height: 267px;
    background: radial-gradient(ellipse 75% 60% at 60% 45%, var(--leaf-on-dark) 0%, rgba(255,255,255,0.08) 55%, rgba(255,255,255,0) 100%);
  }
  .letterhead .branch-decor {
    left: 0; top: 380px; width: 220px; height: 460px;
    background: radial-gradient(ellipse 60% 55% at 25% 50%, var(--leaf-pale) 0%, rgba(228,237,200,0.5) 55%, rgba(228,237,200,0) 100%);
  }

  .card-name, .card-role, .card-contact,
  .letterhead-details, .letter-greeting, .letter-body { z-index: 1; }

  .card-name { position: absolute; left: 18px; top: 178px; font-size: 18px; }
  .card-role { position: absolute; left: 18px; top: 199px; font-size: 12.5px; }
  .card-contact { position: absolute; left: 18px; top: 271px; font-size: 10.5px; line-height: 13.2px; }
  .card-contact .gap { margin-top: 6px; }

  .letterhead { left: 567px; top: 60px; width: 588px; height: 838px; background: var(--paper); }
  .letterhead .wordmark-tile { left: 54px; top: 44px; width: 67px; height: 66px; }
  .letterhead .wordmark-tile .wordmark { font-size: 12.5px; }
  .letterhead-details { position: absolute; left: 136px; top: 79px; font-size: 8.6px; line-height: 11.5px; color: var(--olive); }
  .letter-greeting { position: absolute; left: 54px; top: 201px; font-size: 9.6px; color: var(--ink-soft); }
  .letter-body { position: absolute; left: 54px; top: 256px; width: 478px; font-size: 9.4px; line-height: 12.3px; color: var(--ink-soft); text-align: justify; }
  .letter-body p { margin-bottom: 12px; }
</style>
</head>
<body>

  <div class="wordmark wordmark--on-white"><span class="wordmark-dot"></span>Brivana<br>Fresh<br>Pantry</div>

  <div class="wordmark-tile wordmark-tile--large">
    <div class="wordmark"><span class="wordmark-dot"></span>Brivana<br>Fresh<br>Pantry</div>
  </div>

  <section class="card card--light">
    <div class="branch-decor" role="img" aria-label="Faint olive branch with leaves and an olive, decorative background"></div>
    <div class="wordmark-tile"><div class="wordmark"><span class="wordmark-dot"></span>Brivana<br>Fresh<br>Pantry</div></div>
    <div class="card-name">Marcus Holt</div>
    <div class="card-role">General Manager</div>
    <div class="card-contact">
      Harbour Court, 218<br>Elm Street, Sydney<br>phone: 02 9471 3050<br>fax: 02 9471 3051
      <div class="gap">www.brivana-pantry.au<br>e-mail: hello@brivana-pantry.au</div>
    </div>
  </section>

  <section class="card card--dark">
    <div class="branch-decor" role="img" aria-label="Faint olive branch with leaves, tone on tone decorative background"></div>
    <div class="wordmark-tile"><div class="wordmark"><span class="wordmark-dot"></span>Brivana<br>Fresh<br>Pantry</div></div>
    <div class="card-name">Marcus Holt</div>
    <div class="card-role">General Manager</div>
    <div class="card-contact">
      Harbour Court, 218<br>Elm Street, Sydney<br>phone: 02 9471 3050<br>fax: 02 9471 3051
      <div class="gap">www.brivana-pantry.au<br>e-mail: hello@brivana-pantry.au</div>
    </div>
  </section>

  <section class="letterhead">
    <div class="branch-decor" role="img" aria-label="Faint olive branch with leaves along the left edge, decorative background"></div>
    <div class="wordmark-tile"><div class="wordmark"><span class="wordmark-dot"></span>Brivana<br>Fresh<br>Pantry</div></div>
    <div class="letterhead-details">
      Harbour Court, 218 Elm Street, Sydney<br>
      phone: 02 9471 3050 • fax: 02 9471 3051<br>
      e-mail: hello@brivana-pantry.au • www.brivana-pantry.au
    </div>
    <div class="letter-greeting">Dear, customer!</div>
    <div class="letter-body">
      <p>Thank you for choosing our pantry range, we are glad to welcome you as a partner.</p>
      <p>Our oils are pressed from hand picked olives grown on small family groves, then sealed in dark glass to keep their colour and flavour at their best. Each batch is tasted before it leaves the mill, and we keep records of the harvest, the press date and the storage so that every bottle can be traced back to the grove. We deliver weekly to restaurants, cafes and delis across the city, and our team is always happy to help you choose the right oil for dressings, baking or finishing a plate.</p>
      <p>Please find enclosed our current price list together with the order form for the coming season. New blends will be added in spring and we will send samples to all our regular customers.</p>
      <p>Orders placed before noon on a weekday are packed the same day and arrive within two working days.</p>
      <p>Every product in our range is chosen with care. We visit the growers, walk the groves and taste the oil straight from the press before we agree to carry it. This lets us offer a short list of oils we truly trust, from mild and buttery blends that suit fish and salads to bold, peppery oils that stand up to grilled meat and roasted vegetables. For kitchens that use larger volumes we supply tins and refillable drums, and we collect the empty drums on our next visit to cut waste. We can also arrange tastings for your staff, with notes on each oil and ideas for how to use it on your menu. If you would like a tasting, simply call our office or send us an email and we will find a time that suits your service.</p>
      <p>We look forward to working with you and to bringing fresh, honest oil to your table.</p>
    </div>
  </section>

</body>
</html>
```